Roofing Company Realtor Marketing Flyer

We would like a design for marketing material aimed at realtors. We are seeking to build relationships with local realtors to ensure that both sellers and buyers are happy and confident with their roofing systems through roof inspections, No-Leak certification, roof repairs, and replacements if necessary.

There are three points that must be included:
1. Home inspectors are generalists. We are roof experts that specialize in diagnosing and fixing roofing problems.
2. We offer "No Leak" certification to offer peace of mind to homeowners.
3. We offer referral bonuses for realtors.

Target Market(s)

Realtors

Industry/Entity Type

Roofing

Font styles to use
Sans Serif

Colors

Designer to choose colors to be used in the design.

Requirements
Must have
• Must be double-sided.
• Must be similar to current marketing materials design. See website http://shinglecrestpro.com and attached images for details.
• We would also like a "fanned out" version of our Sample Inspection Report showing glimpses of some of the images on the later pages (See attached documents).

```html
<!DOCTYPE html>
<html lang="en">
<head>
<meta charset="utf-8">
<title>ShingleCrest Pro – Realtor Flyer</title>
<link rel="stylesheet" href="https://fonts.googleapis.com/css2?family=Lato:wght@400;700&family=Michroma&display=swap">
<style>
:root{
  --orange:#f08a24;
  --slate:#58585a;
  --slate-dark:#4a4a4c;
  --paper:#ffffff;
  --mist:#f1f1f1;
  --ink:#2b2b2b;
  --stage:#ebe8e3;
}
*{box-sizing:border-box;margin:0;padding:0}
html,body{width:1200px;height:1200px;overflow:hidden;background:var(--stage);font-family:"Lato",sans-serif;color:var(--ink)}
.sheet{position:absolute;top:260px;width:525px;height:680px;background:var(--paper);overflow:hidden;box-shadow:0 4px 14px rgba(0,0,0,.18)}
.sheet--front{left:47px}
.sheet--back{left:629px}
.abs{position:absolute}
.hero{position:absolute;left:0;top:0;width:525px}
.brand{position:absolute;color:var(--paper);font-family:"Lato",sans-serif;font-weight:400;font-size:29px;letter-spacing:.2px;white-space:nowrap;display:flex;align-items:center;gap:9px}
.brand__dot{width:12px;height:12px;background:var(--orange)}
.front-brand{right:30px;top:38px}
.back-brand{left:24px;top:52px}
.question{left:149px;top:86px;transform:translateX(-50%);text-align:center;font-family:"Michroma",sans-serif;font-size:13.5px;line-height:20px;white-space:nowrap}
.question span{display:block}
.question .q1{color:var(--slate-dark)}
.question .q2{color:var(--orange)}
.promise{left:0;top:368px;width:525px;height:60px;background:var(--orange);color:var(--paper);font-family:"Michroma",sans-serif;font-size:16px;line-height:24px;text-align:center;padding-top:6px;white-space:nowrap}
.service{position:absolute;top:440px;width:114px;text-align:center}
.service__photo{width:114px;height:94px;border:1px solid #999;box-shadow:0 2px 4px rgba(0,0,0,.25)}
.service__name{margin-top:8px;font-size:10.5px;line-height:13px;color:var(--ink)}
.checks{left:0;top:576px;width:525px;height:50px;background:var(--mist)}
.check{position:absolute;display:flex;gap:7px;font-size:8px;line-height:10px;color:var(--ink)}
.check svg{flex:none;width:9px;height:9px;margin-top:1px}
.partner{left:0;top:634px;width:525px;text-align:center;color:var(--orange);font-size:11.5px;font-weight:700}
.footer{left:0;top:654px;width:525px;height:26px;background:var(--slate);display:flex;justify-content:center;align-items:center;gap:22px;color:var(--paper);font-size:8.5px}
.footer span{display:flex;align-items:center;gap:8px}
.footer svg{width:9px;height:9px}
.feature{position:absolute;left:24px;width:477px;display:flex;gap:14px}
.feature__photo{flex:none;width:114px;height:82px;border:1px solid #888}
.feature h3{font-size:10px;font-weight:700;margin:6px 0 8px;color:var(--ink)}
.feature p{font-size:7.4px;line-height:10.3px;text-align:justify;color:#444}
.badges{left:0;top:604px;width:525px;height:50px;background:var(--orange);display:flex;justify-content:space-around;align-items:center;padding:0 40px}
.badge{width:40px;height:40px;border-radius:50%;border:3px solid #fff}
.badge--green{background:#4fa43a}
.badge--blue{background:#2b5fa8}
.badge--red{background:#b22a25}
.badge--bronze{background:#c86d1f}
</style>
</head>
<body>

<section class="sheet sheet--front">
  <svg class="hero" viewBox="0 0 656 460" width="525" height="368">
    <defs>
      <linearGradient id="frontScene" x1="0" y1="0" x2="0" y2="1">
        <stop offset="0" stop-color="#ffffff"/>
        <stop offset=".25" stop-color="#b9d3ee"/>
        <stop offset=".45" stop-color="#cdbfa8"/>
        <stop offset=".85" stop-color="#d8cbb4"/>
        <stop offset="1" stop-color="#4f7a3a"/>
      </linearGradient>
    </defs>
    <rect width="656" height="460" fill="url(#frontScene)" role="img" aria-label="Photo of a large brick two-storey family home with a shingled roof under a blue sky"/>
    <polygon points="0,0 656,0 656,118 346,118 178,22 0,128" fill="#58585a"/>
    <polyline points="0,140 178,32 346,127 656,127" fill="none" stroke="#f08a24" stroke-width="17"/>
    <polygon points="12,140 178,44 330,135 300,160 60,160" fill="#ffffff" opacity=".85"/>
  </svg>
  <div class="brand front-brand"><i class="brand__dot"></i>ShingleCrest Pro</div>
  <div class="abs question"><span class="q1">BUYING OR</span><span class="q2">SELLING A HOUSE?</span></div>

  <div class="abs promise">WE CAN HELP PROTECT YOUR<br>INTERESTS &amp; ADD PROPERTY VALUE</div>

  <div class="service" style="left:45px">
    <div class="service__photo" role="img" aria-label="Photo of a roofer in a hard hat inspecting shingles" style="background:linear-gradient(160deg,#a07552,#6f4a31)"></div>
    <div class="service__name">Roof Analysis &amp;<br>NO-LEAK Certification</div>
  </div>
  <div class="service" style="left:203px">
    <div class="service__photo" role="img" aria-label="Photo of a worker repairing damaged roof shingles" style="background:linear-gradient(160deg,#8a8a8a,#5a5450)"></div>
    <div class="service__name">Leak &amp;<br>Damage Repair</div>
  </div>
  <div class="service" style="left:363px">
    <div class="service__photo" role="img" aria-label="Photo of a crew installing a new roof against a blue sky" style="background:linear-gradient(180deg,#8fb4dc,#e7dccb)"></div>
    <div class="service__name">Roof Replacement</div>
  </div>

  <div class="abs checks">
    <div class="check" style="left:28px;top:10px"><svg viewBox="0 0 10 10"><rect x=".5" y="1.5" width="8" height="8" fill="none" stroke="#f08a24"/><path d="M2.5 5l2 2L9.5 1" fill="none" stroke="#f08a24" stroke-width="1.3"/></svg>Understand the true detail of the roof.</div>
    <div class="check" style="left:28px;top:32px"><svg viewBox="0 0 10 10"><rect x=".5" y="1.5" width="8" height="8" fill="none" stroke="#f08a24"/><path d="M2.5 5l2 2L9.5 1" fill="none" stroke="#f08a24" stroke-width="1.3"/></svg>Cover warranty gaps with our "No-Leak" Certification.</div>
    <div class="check" style="left:272px;top:10px;width:230px"><svg viewBox="0 0 10 10"><rect x=".5" y="1.5" width="8" height="8" fill="none" stroke="#f08a24"/><path d="M2.5 5l2 2L9.5 1" fill="none" stroke="#f08a24" stroke-width="1.3"/></svg>Our expert crews perform the repair and replacement services.</div>
  </div>

  <div class="abs partner">Ask us about our partnership program!</div>

  <div class="abs footer">
    <span><svg viewBox="0 0 10 10"><path d="M2 1l2 2-1 1.2c.6 1.2 1.6 2.2 2.8 2.8L7 6l2 2-1.3 1.5C4.5 9.2.8 5.5.5 2.3z" fill="#f08a24"/></svg>844-ShingleCrest</span>
    <span><svg viewBox="0 0 10 10"><rect x="0" y="2" width="10" height="6.5" fill="#f08a24"/><path d="M0 2l5 3.5L10 2" fill="none" stroke="#58585a" stroke-width=".8"/></svg>info@ShingleCrestPro.com</span>
    <span><svg viewBox="0 0 10 10"><circle cx="5" cy="5" r="4.5" fill="#f08a24"/><path d="M.5 5h9M5 .5c-2.5 3-2.5 6 0 9M5 .5c2.5 3 2.5 6 0 9" fill="none" stroke="#58585a" stroke-width=".6"/></svg>www.ShingleCrestPro.com</span>
  </div>
</section>

<section class="sheet sheet--back">
  <svg class="hero" viewBox="0 0 656 395" width="525" height="316">
    <defs>
      <linearGradient id="backScene" x1="0" y1="0" x2="0" y2="1">
        <stop offset="0" stop-color="#e6ecef"/>
        <stop offset=".35" stop-color="#7f9a6a"/>
        <stop offset=".6" stop-color="#d9dbdc"/>
        <stop offset=".85" stop-color="#b8b3ab"/>
        <stop offset="1" stop-color="#5d8a3e"/>
      </linearGradient>
    </defs>
    <rect width="656" height="395" fill="url(#backScene)" role="img" aria-label="Photo of a white two-storey house with grey roof surrounded by tall trees"/>
    <polygon points="0,0 656,0 656,140 478,22 330,118 0,118" fill="#58585a"/>
    <polyline points="0,127 330,127 478,32 656,150" fill="none" stroke="#f08a24" stroke-width="17"/>
  </svg>
  <div class="brand back-brand"><i class="brand__dot"></i>ShingleCrest Pro</div>

  <div class="feature" style="top:324px">
    <div class="feature__photo" role="img" aria-label="Fanned-out pages of a sample roof inspection report" style="background:linear-gradient(135deg,#2e2e2e,#f4f4f4 55%,#3a3a3a)"></div>
    <div>
      <h3>Understand the true detail of the roof</h3>
      <p>Home inspectors, who are generalists, are often unable to adequately inspect and assess the condition of roofing systems. ShingleCrest's specialists are trained to diagnose roofing problems and recommend solutions to fit any budget. Our expert Advisors carefully investigate all aspects of the roofing system to assess the condition of the roof. After completing the inspection, our Advisors compile a comprehensive report of their findings including images of the roofing system.</p>
    </div>
  </div>
  <div class="feature" style="top:418px">
    <div class="feature__photo" role="img" aria-label="Photo of a roofer nailing shingles" style="background:linear-gradient(160deg,#7b7b7b,#8a5a48)"></div>
    <div>
      <h3>Cover warranty gaps with our “No-Leak” Certification</h3>
      <p>Home warranties typically cover appliances, not roofing systems. What good is a warranty if it doesn't protect your property from top to bottom? Our "No-Leak" Certification provides peace of mind to homeowners</p>
    </div>
  </div>
  <div class="feature" style="top:512px">
    <div class="feature__photo" role="img" aria-label="Photo of hands laying roof tiles" style="background:linear-gradient(160deg,#3f6fa8,#c0765a)"></div>
    <div>
      <h3>Our expert crews perform the repair &amp; replacement services</h3>
      <p>Repair and replacement services aren't just “jobs” to us. We take pride in every step of the process from quote to completion. Our dedicated office staff coordinates with our production team and technicians to ensure quality work and customer satisfaction.</p>
    </div>
  </div>

  <div class="abs badges">
    <div class="badge badge--green"></div>
    <div class="badge badge--blue"></div>
    <div class="badge badge--blue"></div>
    <div class="badge badge--red"></div>
    <div class="badge badge--bronze"></div>
  </div>

  <div class="abs footer">
    <span><svg viewBox="0 0 10 10"><path d="M2 1l2 2-1 1.2c.6 1.2 1.6 2.2 2.8 2.8L7 6l2 2-1.3 1.5C4.5 9.2.8 5.5.5 2.3z" fill="#f08a24"/></svg>844-ShingleCrest</span>
    <span><svg viewBox="0 0 10 10"><rect x="0" y="2" width="10" height="6.5" fill="#f08a24"/><path d="M0 2l5 3.5L10 2" fill="none" stroke="#58585a" stroke-width=".8"/></svg>info@ShingleCrestPro.com</span>
    <span><svg viewBox="0 0 10 10"><circle cx="5" cy="5" r="4.5" fill="#f08a24"/><path d="M.5 5h9M5 .5c-2.5 3-2.5 6 0 9M5 .5c2.5 3 2.5 6 0 9" fill="none" stroke="#58585a" stroke-width=".6"/></svg>www.ShingleCrestPro.com</span>
  </div>
</section>

</body>
</html>
```